Pellham Ridge Nectar Company, local Honey producer needs product Lable to encourage sales

We are a small business (Pellham Ridge Nectar Company) located in a small Texas town that harvests honey from our beehives yearly. Our honey would be considered "raw wildflower honey" and our goal is to sell it locally (farmers markets) and to surrounding areas.

We are currently packaging in plastic classic honey bottles with white flip caps. Sizes are 8oz and 16oz bottles (see pictures for actual size). Larger orders will be filled in one quart mason jars.

Design Ideas:
-vintage style design with bee or several bees in background
- incorporate company name "Pellham Ridge Nectar Company"
- needs small description "Raw Honey", and "Harvested in Cedarmoor, Texas"

Target Market(s)

Farmers markets, health conscience people looking for unprocessed food options

Industry/Entity Type

Small Business

Requirements
Nice to have
• Vintage feel
Should not have
• No cartoonish characters

```html
<!DOCTYPE html>
<html lang="en">
<head>
<meta charset="utf-8">
<title>Pellham Ridge Nectar Company – Raw Honey Label</title>
<link rel="stylesheet" href="https://fonts.googleapis.com/css2?family=Josefin+Sans:wght@600;700&family=Oswald:wght@500&family=Cinzel:wght@600&display=swap">
<style>
  :root {
    --page: #ffffff;
    --rim-top: #031203;
    --rim-bottom: #6db61a;
    --panel-top: #0e2a09;
    --panel-mid: #3d7a12;
    --panel-bottom: #86c925;
    --hex-line: #d4a9bd;
    --name-ink: #55485a;
    --accent-tan: #c9a67a;
    --bee-dark: #7a3d10;
    --bee-light: #d9c62a;
  }
  html, body {
    margin: 0;
    padding: 0;
    width: 1200px;
    height: 1200px;
    overflow: hidden;
    background: var(--page);
  }
  .label-canvas {
    display: block;
    width: 1200px;
    height: 1200px;
  }
  .label-rim { fill: url(#rimGradient); }
  .label-panel { fill: url(#panelGradient); stroke: rgba(230,240,200,0.35); stroke-width: 2; }
  .bee-window { fill: url(#beeGradient); stroke: rgba(0,0,0,0.35); stroke-width: 2; }
  .hex-frame { fill: none; stroke: var(--hex-line); stroke-width: 6; }
  .rule { stroke: var(--accent-tan); stroke-width: 2.5; }
  .tagline-top {
    font-family: "Josefin Sans", sans-serif;
    font-weight: 700;
    font-size: 36px;
    letter-spacing: 10px;
    fill: var(--accent-tan);
  }
  .company-name {
    font-family: "Josefin Sans", sans-serif;
    font-weight: 600;
    font-size: 42px;
    letter-spacing: 3px;
    fill: var(--name-ink);
    stroke: #cfc3c9;
    stroke-width: 0.8;
  }
  .harvest-line {
    font-family: "Oswald", sans-serif;
    font-weight: 500;
    font-size: 32px;
    letter-spacing: 2px;
    fill: var(--accent-tan);
  }
  .state-name {
    font-family: "Cinzel", serif;
    font-weight: 600;
    font-size: 26px;
    letter-spacing: 14px;
    fill: var(--accent-tan);
  }
</style>
</head>
<body>
<svg class="label-canvas" viewBox="0 0 1200 1200" xmlns="http://www.w3.org/2000/svg">
  <defs>
    <linearGradient id="rimGradient" x1="0" y1="0" x2="0" y2="1">
      <stop offset="0" stop-color="var(--rim-top)"/>
      <stop offset="0.45" stop-color="#1c4a0c"/>
      <stop offset="1" stop-color="var(--rim-bottom)"/>
    </linearGradient>
    <linearGradient id="panelGradient" x1="0" y1="0" x2="0" y2="1">
      <stop offset="0" stop-color="var(--panel-top)"/>
      <stop offset="0.5" stop-color="var(--panel-mid)"/>
      <stop offset="1" stop-color="var(--panel-bottom)"/>
    </linearGradient>
    <linearGradient id="beeGradient" x1="0" y1="0" x2="0" y2="1">
      <stop offset="0" stop-color="var(--bee-dark)"/>
      <stop offset="0.5" stop-color="#a86a1c"/>
      <stop offset="1" stop-color="var(--bee-light)"/>
    </linearGradient>
    <path id="arcTop" d="M 430 604 Q 600 540 770 604"/>
    <path id="arcBottom" d="M 512 866 Q 600 918 688 866"/>
  </defs>

  <rect class="label-rim" x="290" y="122" width="624" height="950" rx="312" ry="312"/>
  <rect class="label-panel" x="310" y="140" width="580" height="908" rx="290" ry="290"/>

  <ellipse class="bee-window" cx="600" cy="306" rx="160" ry="106" role="img" aria-label="Illustration of a honeybee standing on honeycomb"/>

  <polygon class="hex-frame" points="600,444 832,576 832,848 600,982 368,848 368,576"/>

  <text class="tagline-top" text-anchor="middle"><textPath href="#arcTop" startOffset="50%">RAW HONEY</textPath></text>
  <line class="rule" x1="452" y1="614" x2="540" y2="614"/>
  <line class="rule" x1="648" y1="614" x2="736" y2="614"/>

  <text class="company-name" x="600" y="696" text-anchor="middle" textLength="370" lengthAdjust="spacingAndGlyphs">PELLHAM RIDGE</text>
  <text class="company-name" x="600" y="748" text-anchor="middle" textLength="390" lengthAdjust="spacingAndGlyphs">NECTAR COMPANY</text>

  <text class="harvest-line" x="600" y="812" text-anchor="middle" textLength="342" lengthAdjust="spacingAndGlyphs">HARVESTED IN CEDARMOOR</text>
  <line class="rule" x1="450" y1="842" x2="540" y2="842"/>
  <line class="rule" x1="648" y1="842" x2="738" y2="842"/>

  <text class="state-name" text-anchor="middle"><textPath href="#arcBottom" startOffset="50%">TEXAS</textPath></text>
</svg>
</body>
</html>
```